Design some Business Cards

***WINNER MUST PROVIDE LAYERED PSD FILE(S)***

This is for a business that is about to launch and needs a GREAT business card design.

You can see the website draft here: http://kovta812.client.ferntop583.com/

Use the website to help understand how the look and feel of the cards should be and get ideas for the design.

The slogan is "Real Estate Investing at a Push of a Button"

Logo is attached

Winner will also get a chance to design:

Flyer
Vertical Banner
Trade Show (Expo) Display
Brochure

Good Luck!

```html
<!DOCTYPE html>
<html lang="en">
<head>
<meta charset="utf-8">
<title>kovta812 Business Cards</title>
<link rel="stylesheet" href="https://fonts.googleapis.com/css2?family=Open+Sans:wght@400;600&display=swap">
<style>
  :root {
    --bg: #1b1b1b;
    --brand-red: #e0282e;
    --paper: #ffffff;
    --ink: #3a3a3a;
    --ink-soft: #555555;
  }
  * { margin: 0; padding: 0; box-sizing: border-box; }
  html, body {
    width: 1200px; height: 900px; overflow: hidden;
    background: var(--bg);
    font-family: "Open Sans", Arial, sans-serif;
  }
  .stage { position: relative; width: 1200px; height: 900px; }
  .card {
    position: absolute; left: 320px; width: 560px; height: 320px; overflow: hidden;
  }
  .card--front { top: 90px; background: var(--paper); }
  .card--back { top: 490px; background: var(--brand-red); display: flex; align-items: center; justify-content: center; }

  .front__band {
    position: absolute; left: 0; bottom: 0; width: 560px; height: 130px; background: var(--brand-red);
  }
  .front__column {
    position: absolute; left: 0; top: 0; width: 170px; height: 320px; background: var(--brand-red);
    z-index: 1;
  }
  .front__rule {
    position: absolute; left: 14px; top: 0; width: 2px; height: 320px; background: var(--paper);
    z-index: 2;
  }
  .front__social {
    position: absolute; left: 28px; top: 22px; display: flex; gap: 6px; z-index: 2;
  }
  .front__social span { width: 14px; height: 14px; background: var(--paper); display: block; }
  .contact-list {
    position: absolute; left: 28px; top: 56px; width: 138px; list-style: none;
    color: var(--paper); font-size: 10.5px; line-height: 1; z-index: 2;
  }
  .contact-list li { display: flex; align-items: center; gap: 6px; margin-bottom: 12px; white-space: nowrap; }
  .contact-list svg { width: 11px; height: 11px; flex: none; }
  .front__logo {
    position: absolute; right: 30px; top: 40px;
    font-size: 70px; font-weight: 400; color: var(--ink); letter-spacing: -1px; line-height: 1;
  }
  .front__name-box {
    position: absolute; left: 190px; top: 138px; width: 200px; height: 44px;
    background: var(--brand-red); color: var(--paper);
    font-size: 22px; font-weight: 600; display: flex; align-items: center; justify-content: center;
  }
  .front__title-box {
    position: absolute; left: 190px; top: 182px; width: 236px; height: 34px;
    background: var(--paper); color: var(--ink-soft);
    font-size: 15px; display: flex; align-items: center; padding-left: 24px;
  }
  .front__address {
    position: absolute; right: 26px; bottom: 26px; text-align: right; font-style: normal;
    color: var(--paper); font-size: 13px; line-height: 1.4;
  }
  .back__logo {
    font-size: 92px; font-weight: 400; color: var(--paper); letter-spacing: -1px;
  }
</style>
</head>
<body>
<main class="stage">
  <section class="card card--front" aria-label="Business card front">
    <div class="front__band"></div>
    <div class="front__column"></div>
    <div class="front__rule"></div>
    <div class="front__social"><span></span><span></span><span></span></div>
    <ul class="contact-list">
      <li><svg viewBox="0 0 12 12"><path fill="#fff" d="M3 1l2 2-1 1.5c.8 1.5 2 2.7 3.5 3.5L9 7l2 2-1.5 2C5 10.5 1.5 7 1 2.5z"/></svg>(250) 555-0148</li>
      <li><svg viewBox="0 0 12 12"><path fill="#fff" d="M3 1l2 2-1 1.5c.8 1.5 2 2.7 3.5 3.5L9 7l2 2-1.5 2C5 10.5 1.5 7 1 2.5z"/></svg>(250) 555-0192</li>
      <li><svg viewBox="0 0 12 12"><rect x="1" y="3" width="10" height="7" fill="none" stroke="#fff"/><path d="M1 3l5 4 5-4" fill="none" stroke="#fff"/></svg>dale@harlowpanel.com</li>
      <li><svg viewBox="0 0 12 12"><circle cx="6" cy="6" r="5" fill="none" stroke="#fff"/><path d="M1 6h10M6 1c-3 3-3 7 0 10M6 1c3 3 3 7 0 10" fill="none" stroke="#fff"/></svg>www.harlowpanel.com</li>
    </ul>
    <div class="front__logo">kovta812</div>
    <div class="front__name-box">Dale Pruitt</div>
    <div class="front__title-box">Repair Planner</div>
    <address class="front__address">2271 Copperline Rd, Vernwick,<br>BC V0X 4K2</address>
  </section>

  <section class="card card--back" aria-label="Business card back">
    <div class="back__logo">kovta812</div>
  </section>
</main>
</body>
</html>
```